lunetra.com redesign

We are a successful web hosting company that has been around since 1999 with 10,000 customers managing 2,000 websites and 12,000 domain names. Our challenge - we are losing ground because our site is getting old, our pricing is not competitive and our feature set needs to change to match the new world of mobile centric everything. We want to reach out to all of the domain names that we don't host websites for. We believe that if we designed a new site that focuses on bringing home all of those externally hosted websites to our own web hosting company that we would have a solid future. We need to compete against mopwizzle.com, vantrimble.com, kerbloom.com, zinqhut.com, nolvark.com, brimfolk.com, quorvane.com, welbix.com and 100,000 others. We need to simplify our message with clean design, focused pages, easy decision making processes for the consumer. We use WHMCS for the background provisioning and billing so we can pretty much manage any kind of pricing model and discounted promotion packages.
I would prefer Twitter bootstrap CSS based responsive design.

Reason: I was away on vacation for 2 weeks - I just got back - I need time to fairly review all submissions - thank you for your patience. Dorian Fenwick Lunetra.com

Thanks to all who submitted sample designs - unfortunately most of them were nothing much more than already available templates with some of my current content and logo added to them. I will try to be more specific to reduce the number of choices. I need the template be fully compatible with WHMCS and Wordpress if you can't make it work with WHMCS directly. Another question I have to ask is -"exactly what am I getting for my $500.00 - is it just a PSD template or actual integration of that theme into WHMCS or Wordpress?"  I don't expect anyone to create new content for the site at that price. What do you charge if  you are able to create content or get directly involved in the site implementation of that template?

```html
<!DOCTYPE html>
<html lang="en">
<head>
<meta charset="utf-8">
<title>Lunetra — Domains and Hosting</title>
<link href="https://fonts.googleapis.com/css2?family=Open+Sans:wght@300;400;600;700&display=swap" rel="stylesheet">
<style>
:root{
  --header:#2b4460;
  --header-top:#1f3349;
  --accent:#29a9d9;
  --accent-light:#3fc0e6;
  --cyan-band:#3cc3e3;
  --navy:#2c4761;
  --navy-deep:#1c2d40;
  --ink:#333b44;
  --muted:#7b858f;
  --line:#e3e6e9;
  --paper:#ffffff;
  --soft:#f3f4f5;
  --table-head:#2e4a66;
}
*{box-sizing:border-box;margin:0;padding:0}
html,body{width:1200px;height:2659px;overflow:hidden}
body{font-family:"Open Sans",Arial,sans-serif;color:var(--ink);background:var(--paper);position:relative}

/* Header */
.site-header{position:absolute;left:0;top:0;width:1200px;height:79px;background:linear-gradient(var(--header),var(--header-top))}
.utility-links{position:absolute;right:163px;top:4px;display:flex;font-size:10px;color:#c9d4de;white-space:nowrap}
.utility-links span{padding:0 10px;border-left:1px solid #4d6680}
.utility-links span:first-child{border-left:none}
.login-tab{position:absolute;left:988px;top:2px;width:49px;height:16px;background:var(--accent);color:#fff;font-size:10px;text-align:center;line-height:16px;border-radius:2px}
.brand{position:absolute;left:163px;top:24px;font-size:31px;font-weight:700;color:#fff;letter-spacing:-0.5px;line-height:40px}
.main-nav{position:absolute;left:459px;top:22px;display:flex;height:57px;white-space:nowrap}
.main-nav a{color:#fff;text-decoration:none;font-size:11px;font-weight:600;padding:0 12px;line-height:57px}
.main-nav a.active{background:var(--accent);width:60px;padding:0;text-align:center}
.login-box{position:absolute;left:894px;top:38px;width:143px;height:78px;background:#fff;border:1px solid #cfd5da;box-shadow:0 2px 6px rgba(0,0,0,.25);padding:8px}
.login-box .field{height:14px;background:#e7eaed;border:1px solid #d4d8dc;font-size:8px;color:#9aa3ab;padding-left:4px;line-height:12px;margin-bottom:4px}
.login-box .reset{position:absolute;left:8px;top:52px;font-size:8px;color:#7b858f;line-height:10px}
.login-box .go{position:absolute;right:8px;top:52px;width:42px;height:16px;background:var(--accent);color:#fff;font-size:9px;text-align:center;line-height:16px}

/* Hero */
.hero{position:absolute;left:0;top:79px;width:1200px;height:470px;background:radial-gradient(ellipse at 50% 40%,#3bb8e2 0%,#1d8cc6 55%,#136aa6 100%)}
.hero-globe{position:absolute;left:190px;top:35px;width:320px;height:320px;border-radius:50%;background:radial-gradient(circle at 40% 35%,#ffffff 0%,#bfe4f6 40%,#3a8fc8 100%)}
.hero-shadow{position:absolute;left:240px;top:385px;width:220px;height:26px;border-radius:50%;background:rgba(0,40,80,.25)}
.hero-copy{position:absolute;left:555px;top:120px;color:#fff}
.hero-copy h1{font-weight:300;font-size:47px;line-height:52px}
.hero-copy h2{font-weight:300;font-size:30px;line-height:34px}
.hero-copy p{font-weight:300;font-size:19px;line-height:25px;margin-top:20px;color:#e4f4fb}
.btn-start{position:absolute;left:559px;top:307px;width:137px;height:43px;background:var(--navy);color:#fff;font-size:17px;text-align:center;line-height:43px;border-radius:2px}
.hero-arrow{position:absolute;top:200px}

/* Domain search band */
.domain-search{position:absolute;left:0;top:549px;width:615px;height:173px;background:var(--cyan-band)}
.domain-search h3{position:absolute;left:150px;top:20px;font-size:27px;font-weight:600;color:#0f2233;line-height:36px;white-space:nowrap}
.domain-search .hint{position:absolute;left:152px;top:56px;font-size:11px;color:#0f2233;font-weight:600}
.domain-search .prefix{position:absolute;left:150px;top:94px;font-size:16px;color:#fff;font-weight:700}
.domain-search .input{position:absolute;left:203px;top:92px;width:307px;height:28px;background:#fff;font-size:11px;color:#a0a8b0;padding-left:10px;line-height:28px}
.domain-search .btn{position:absolute;left:510px;top:92px;width:79px;height:28px;background:linear-gradient(#fff,#dfe6ec);font-size:15px;font-weight:600;color:#1e5c8a;text-align:center;line-height:28px}
.domain-search .sale{position:absolute;left:152px;top:138px;font-size:12px;color:#0f2233;font-weight:600}

.premium{position:absolute;left:615px;top:549px;width:585px;height:173px;background:linear-gradient(90deg,#2a4865,#1e3550)}
.premium .title{position:absolute;left:32px;top:16px;color:#fff;font-size:21px;font-weight:300;white-space:nowrap}
.premium .price{position:absolute;left:32px;top:42px;color:#fff;font-size:27px;font-weight:400;white-space:nowrap}
.premium .plan{position:absolute;left:32px;top:84px;color:#e3ebf2;font-size:12px}
.premium ul{position:absolute;top:106px;list-style:none;color:#dbe4ec;font-size:10px;line-height:20px}
.premium ul li::before{content:"•";margin-right:8px}
.server-art{position:absolute;left:312px;top:13px;width:80px;height:150px;background:linear-gradient(90deg,#111820,#3b4550 50%,#111820);border-radius:3px}

/* Packages */
.packages-title{position:absolute;left:0;top:768px;width:1200px;text-align:center;font-size:24px;font-weight:300;color:#4a525a}
.pkg-table{position:absolute;left:225px;top:849px;width:750px}
.pkg-row{position:absolute;left:0;width:750px;height:34px;border-bottom:1px solid var(--line)}
.pkg-cell{position:absolute;top:0;width:150px;height:34px;text-align:center;line-height:34px;font-size:12px;color:#8a939b;border-left:1px solid var(--line)}
.pkg-head{background:var(--table-head);border-bottom:none}
.pkg-head .pkg-cell{color:#d9e4ee;border-left:1px solid #3c5a78}
.btn-choose{display:inline-block;width:58px;height:16px;line-height:16px;font-size:10px;color:#fff;background:var(--table-head);border-radius:2px;vertical-align:middle}
.pkg-featured{position:absolute;left:675px;top:834px;width:150px;height:229px;background:#fff;box-shadow:0 0 10px rgba(0,0,0,.18)}
.pkg-featured .head{height:33px;background:var(--accent);color:#fff;text-align:center;line-height:33px;font-size:13px}
.pkg-featured .cell{height:39px;border-bottom:1px solid var(--line);text-align:center;line-height:39px;font-size:13px;color:#555}
.pkg-featured .btn-choose{background:var(--accent)}

/* Features */
.features{position:absolute;left:0;top:1119px;width:1200px;height:351px;background:var(--soft)}
.features-photo{position:absolute;left:178px;top:0;width:385px;height:351px;background:linear-gradient(90deg,#bfc3c6,#8b9094 50%,#c9cdd0)}
.feature-item{position:absolute;left:596px;width:385px;height:71px;border-bottom:1px solid #dfe2e5}
.feature-item .num{position:absolute;left:0;top:14px;width:24px;height:24px;border-radius:50%;background:var(--accent);color:#fff;font-size:12px;font-weight:700;text-align:center;line-height:24px}
.feature-item h4{position:absolute;left:40px;top:10px;font-size:13px;font-weight:600;color:#27415c}
.feature-item p{position:absolute;left:40px;top:28px;font-size:11px;color:#6a737c;white-space:nowrap}

/* Free services */
.services{position:absolute;left:0;top:1470px;width:1200px;height:353px;background:radial-gradient(ellipse at 50% 40%,#2fb2df,#1a89c2 60%,#1670a8)}
.services h2{position:absolute;left:0;top:42px;width:1200px;text-align:center;color:#0f2a40;font-size:26px;font-weight:300;line-height:30px}
.services h2 b{font-weight:400;display:block}
.service{position:absolute;top:145px;width:200px;text-align:center;color:#fff}
.service h5{font-size:13px;font-weight:400;color:#e8f6fc;margin-bottom:16px}
.service svg{display:block;margin:0 auto 18px}
.service p{font-size:11px;line-height:15px;color:#f1f9fd;padding:0 20px}

/* Info */
.info{position:absolute;left:0;top:1823px;width:1200px;height:699px;background:var(--navy)}
.info h2{position:absolute;left:0;top:46px;width:1200px;text-align:center;color:#d6e2ec;font-size:26px;font-weight:300;line-height:30px}
.info-col{position:absolute;top:160px;width:360px}
.info-block{margin-bottom:30px}
.info-block h5{font-size:13px;font-weight:400;color:#e1e9f0;margin-bottom:14px}
.info-block p{font-size:10px;line-height:15px;color:#a9bac9}
.info-block p b{color:#fff;font-weight:600}
.badge-shape{position:absolute;left:896px;top:2083px;width:56px;height:56px;border-radius:50%;background:#1d3b6e;border:4px solid #e6eef5}

/* Footer */
.site-footer{position:absolute;left:0;top:2522px;width:1200px;height:137px;background:var(--navy-deep);text-align:center;color:#7f92a3;font-size:9.5px}
.site-footer .links{position:absolute;top:25px;width:1200px}
.site-footer .copy{position:absolute;top:40px;width:1200px}
.pay-cards{position:absolute;left:550px;top:60px;display:flex;gap:4px}
.pay-cards span{width:30px;height:16px;border-radius:2px;background:#e9eef2}
.site-footer .terms{position:absolute;top:90px;width:1200px;line-height:13px}
.to-top{position:absolute;left:940px;top:45px;width:34px;height:34px;background:#0d1620}
</style>
</head>
<body>

<header class="site-header">
  <nav class="utility-links">
    <span>Company</span><span>Partners</span><span>Support</span><span>Contact Us</span><span>Shopping Cart</span><span>References</span><span>Pricing</span>
  </nav>
  <div class="login-tab">Login</div>
  <div class="brand">Lunetra</div>
  <nav class="main-nav">
    <a class="active">Home</a><a>Domain Name Center</a><a>Web Site Hosting Center</a><a>S.E.O. Toolkit</a>
  </nav>
</header>
<div class="login-box">
  <div class="field">Email Address</div>
  <div class="field">••••••••</div>
  <div class="reset">Request<br>Password Reset</div>
  <div class="go">Login</div>
</div>

<section class="hero">
  <svg class="hero-arrow" style="left:100px" width="24" height="56" viewBox="0 0 24 56"><path d="M22 2 L2 28 L22 54" fill="none" stroke="#fff" stroke-width="2"/></svg>
  <svg class="hero-arrow" style="left:1070px" width="24" height="56" viewBox="0 0 24 56"><path d="M2 2 L22 28 L2 54" fill="none" stroke="#fff" stroke-width="2"/></svg>
  <div class="hero-shadow"></div>
  <div class="hero-globe" role="img" aria-label="Glossy globe with a web address bar and cursor"></div>
  <div class="hero-copy">
    <h1>Free domain name</h1>
    <h2>with every new hosting package.</h2>
    <p>Sign up for one affordable hosting packages,<br>and your top-level domain is on us.</p>
  </div>
  <div class="btn-start">Start Now</div>
</section>

<section class="domain-search">
  <h3>Find your domain name !</h3>
  <div class="hint">Enter a Domain Name</div>
  <div class="prefix">www.</div>
  <div class="input">Your name.com</div>
  <div class="btn">Search</div>
  <div class="sale">Sale! Premium top-level domain names from $15/year.</div>
</section>
<section class="premium">
  <div class="title">Premium Business Hosting</div>
  <div class="price">From $90/year.</div>
  <div class="plan">Lunetra's e-Lite plan:</div>
  <ul style="left:36px"><li>Domain Name</li><li>100 Mb Space</li><li>5 GB Transfer</li></ul>
  <ul style="left:134px"><li>Unlimited Email Accounts</li><li>Unlimited Aliases</li><li>Dedicated Support</li></ul>
  <div class="server-art" role="img" aria-label="Black rack server unit with a blue light"></div>
</section>

<h2 class="packages-title">Choose A Hosting Package</h2>
<div class="pkg-table">
  <div class="pkg-row pkg-head" style="top:0">
    <div class="pkg-cell" style="left:0;border-left:none"></div>
    <div class="pkg-cell" style="left:150px">e-Lite</div>
    <div class="pkg-cell" style="left:300px">e-200</div>
    <div class="pkg-cell" style="left:600px">e-1000</div>
  </div>
  <div class="pkg-row" style="top:32px">
    <div class="pkg-cell" style="left:0">Storage</div><div class="pkg-cell" style="left:150px">100 Mb</div><div class="pkg-cell" style="left:300px">200 Mb</div><div class="pkg-cell" style="left:600px;border-right:1px solid var(--line)">1000 Mb</div>
  </div>
  <div class="pkg-row" style="top:66px">
    <div class="pkg-cell" style="left:0">Domain Name</div><div class="pkg-cell" style="left:150px">Included</div><div class="pkg-cell" style="left:300px">Included</div><div class="pkg-cell" style="left:600px;border-right:1px solid var(--line)">Included</div>
  </div>
  <div class="pkg-row" style="top:100px">
    <div class="pkg-cell" style="left:0">eMail Accounts</div><div class="pkg-cell" style="left:150px">Unlimited</div><div class="pkg-cell" style="left:300px">Unlimited</div><div class="pkg-cell" style="left:600px;border-right:1px solid var(--line)">Unlimited</div>
  </div>
  <div class="pkg-row" style="top:134px">
    <div class="pkg-cell" style="left:0">Annual Price</div><div class="pkg-cell" style="left:150px">$90</div><div class="pkg-cell" style="left:300px">$149</div><div class="pkg-cell" style="left:600px;border-right:1px solid var(--line)">$549</div>
  </div>
  <div class="pkg-row" style="top:168px">
    <div class="pkg-cell" style="left:0"></div><div class="pkg-cell" style="left:150px"><span class="btn-choose">Choose</span></div><div class="pkg-cell" style="left:300px"><span class="btn-choose">Choose</span></div><div class="pkg-cell" style="left:600px;border-right:1px solid var(--line)"><span class="btn-choose">Choose</span></div>
  </div>
</div>
<div class="pkg-featured">
  <div class="head">e-500</div>
  <div class="cell">500 Mb</div>
  <div class="cell">Included</div>
  <div class="cell">Unlimited</div>
  <div class="cell">$249</div>
  <div class="cell" style="border-bottom:none"><span class="btn-choose">Choose</span></div>
</div>

<section class="features">
  <div class="features-photo" role="img" aria-label="Black and white portrait photo of a smiling man"></div>
  <div class="feature-item" style="top:34px"><div class="num">1</div><h4>Secure Your Domain Name</h4><p>Register, renew, transfer or search your domain name</p></div>
  <div class="feature-item" style="top:105px"><div class="num">2</div><h4>Effective Website Development</h4><p>PageStack Web Builder, Small Business Bundle and Custom Design</p></div>
  <div class="feature-item" style="top:176px"><div class="num">3</div><h4>Web Site Hosting</h4><p>Reliable, affordable options, Real People - real support</p></div>
  <div class="feature-item" style="top:247px"><div class="num">4</div><h4>Market Your Web Site</h4><p>Professional implementation of Search Engine Positioning</p></div>
</section>

<section class="services">
  <h2>Get these free services and many more <b>with all accounts</b></h2>
  <div class="service" style="left:219px">
    <h5>Easy Transfer</h5>
    <svg width="44" height="34" viewBox="0 0 44 34" fill="none" stroke="#fff" stroke-width="2"><rect x="4" y="4" width="36" height="22"/><path d="M14 32h16M22 26v6M14 15h16M25 11l5 4-5 4"/></svg>
    <p>Switching to Lunetra from another host is easy: sit back while we take care of everything.</p>
  </div>
  <div class="service" style="left:406px">
    <h5>Site Builder</h5>
    <svg width="44" height="34" viewBox="0 0 44 34" fill="none" stroke="#fff" stroke-width="2"><rect x="5" y="4" width="34" height="26"/><path d="M5 11h34M12 17h8v8h-8zM24 17h10M24 22h10"/></svg>
    <p>With SiteBuilder, you can build your website with drag-and-drop simplicity.</p>
  </div>
  <div class="service" style="left:594px">
    <h5>Installation</h5>
    <svg width="44" height="34" viewBox="0 0 44 34" fill="none" stroke="#fff" stroke-width="2"><circle cx="22" cy="19" r="11"/><path d="M22 19v-6M19 4h6"/></svg>
    <p>Over 50 essential scripts for building your website installed in minutes with a click.</p>
  </div>
  <div class="service" style="left:781px">
    <h5>BeFound</h5>
    <svg width="44" height="34" viewBox="0 0 44 34" fill="#fff"><path d="M6 14 L38 4 L28 32 L22 20 Z"/></svg>
    <p>We include search engine positioning with every plan, so your customers can find your website.</p>
  </div>
</section>

<section class="info">
  <h2>lunetra make it easy<br>to get online</h2>
  <div class="info-col" style="left:225px">
    <div class="info-block"><h5>About Lunetra</h5><p>As an Domreg-accredited registrar for more than 15 years, Lunetra is a leading provider of <b>domain registration</b>, <b>website hosting</b>, <b>website design</b>, and <b>email hosting</b> for small and medium-sized businesses. Lunetra has helped tens of thousands of businesses and individuals establish their web presence, build their websites, and drive revenue.</p></div>
    <div class="info-block"><h5>Domain Registration</h5><p><b>Registering a domain</b> is the first step in building your website. Choose from dozens of domain extensions such as .com, .net, .us, .biz, .org, .ca and .us. Lunetra offers competitive prices, easy domain search and registration, auto-renewal and domain transfers.</p></div>
    <div class="info-block"><h5>Website Hosting</h5><p>Lunetra's <b>website hosting plans</b> are fast, flexible and affordable. We offer plans to meet your varying bandwidth and disk space requirements. All web hosting plans include free setup, one-click install web applications, and SiteBuilder, our do-it-yourself website building tool. Create a strong online web presence with Lunetra hosting.</p></div>
    <div class="info-block"><h5>Email Hosting</h5><p><b>Email hosting</b> lets you create personalized email accounts at the domain of your choice. Custom email addresses are an important part of building your online brand identity and demonstrating that you are a professional, web-savvy business. Lunetra includes email hosting in all business plans.</p></div>
  </div>
  <div class="info-col" style="left:622px">
    <div class="info-block"><h5>SiteBuilder</h5><p>Included free with every hosting plan, Lunetra's premium <b>SiteBuilder</b> lets anyone easily create a business-quality website. Hundreds of professional templates are available.</p></div>
    <div class="info-block" style="width:250px"><h5>Business Solutions</h5><p>Lunetra provides a variety of business and marketing solutions for small business customers. Some of these products include <b>Website Builder</b> and <b>Business Hosting</b> bundles and our extensive <b>Search Engine Optimization</b> tool kit.</p></div>
    <div class="info-block"><h5>24/7 Customer Service</h5><p>All Lunetra products come with free 24/7 support. For more information about Lunetra customer support, visit the <b>Support</b> section of this website.</p></div>
    <div class="info-block"><h5>More Reasons to Choose Lunetra</h5><p>As an award winning, premium provider of Internet services for small businesses and individuals, Lunetra offers best in class products, dedicated customer support and the highest service reliability available. Choose Lunetra and start building you website today.<br><br>Lunetra has been recognized as a leader in business <b>domain name registration</b> and <b>business hosting</b>. Read what others are saying about us <b>here</b>, <b>here</b> and <b>here</b>.</p></div>
  </div>
</section>
<div class="badge-shape" role="img" aria-label="Award badge"></div>

<footer class="site-footer">
  <div class="links">Terms of Use — Dispute Policy — Disclaimer — Privacy Policy — Refund Policy — Refund Policy — SNST Newsletter</div>
  <div class="copy">Copyright © 2014 Lunetra.com. All Rights Reserved.</div>
  <div class="pay-cards" role="img" aria-label="Accepted payment cards"><span></span><span></span><span></span></div>
  <div class="terms">All Transactions are based on US or Canadian Dollars, lunetra.com is registered and located in Canada<br>90 day refund guarantee on all purchases. No refunds on hosting services already provided.</div>
  <div class="to-top"><svg width="34" height="34" viewBox="0 0 34 34" fill="none" stroke="#8799aa" stroke-width="1.5"><circle cx="17" cy="17" r="8"/><path d="M13 19l4-4 4 4"/></svg></div>
</footer>

</body>
</html>
```